VELORA ARENA CHANNEL-Where being an athlete is a STATE OF MIND-NOT A GENDER

WEBSITE AND OTT NETWORK DEDICATED TO WOMENS SPORTS
VELORA ARENA CHANNEL intends to address the needs of this underserved market in women’s sports media coverage by uniquely delivering 24/7 focused coverage to those interested specifically in women’s sports and related stories, in a more direct and customer driven way.

Our product provides the following solutions:
1. Provides programming to an underserved market
2. Provides expansive exposure (a critical ingredient) for the success of professional women’s sports
3. Values the athletic achievement of female athletes

This will be accomplished in two phases:
Phase 1
Create a dynamic website dedicated to women’s sports featuring up to date scores, highlights and news.
Phase 2
1. Create a full-spectrum OTT (over the top) network that reflects the dynamic and changing nature of women’s athletics, providing innovative programming, helpful information, community and individual experiences, entertainment and a touch of much-needed humor.
2. Create a network dedicated to women’s sports and entertainment that features steady rotation of daily news and highlights of women’s sports delivered by a majority of women reporters. A sports channel for women by women.
3. To offer live, pre-taped, original and diverse programming 24 hours a day seven days a week, 365 days a year.

VVELORA ARENA CHANNEL website “ Veloratv.net “ fills a need to help women’s sports and entertainment enthusiasts get the complete array of scores and highlights they are craving to make the most of their viewing time online. Stats
So VeloraTV.net plans to go above and beyond what the current sports driven websites offer. But beyond what we will offer the consumer, we are also providing an incredible platform for women in sports to showcase their talent to a starved underserved crowd of sports fans.
No matter what your age or skill level or even education, people are searching the web to find specific information, products, and services that interest them. Recognizing the magnitude of our target market that are searching the Internet for various information we realize the importance of meeting their needs with opportunities to discover who we are and what we do. With every search, every click and every download we will be able to get one step closer to our target market.

Target Market(s)

people interested in womens sports

Number of Pages Required

4 page

Font styles to use
Serif

Requirements
Must have
• home page design exactly like www.brisklanegames.net and the ott page (watch page) similar to streamora page, all with womens sports in mind
Nice to have
• view brisklanegames and streamora. Color coordinate to logo

```html
<!DOCTYPE html>
<html lang="en">
<head>
<meta charset="utf-8">
<title>Velora Arena Channel – Home</title>
<link href="https://fonts.googleapis.com/css2?family=Oswald:wght@400;500;600;700&family=Open+Sans:wght@400;600;700&display=swap" rel="stylesheet">
<style>
:root{
  --red:#e2261f;
  --red-dark:#b81b15;
  --ink:#222;
  --text:#555;
  --muted:#888;
  --line:#ddd;
  --page:#f3f3f3;
  --white:#fff;
  --night:#1d1d1d;
  --night-2:#2a2a2a;
}
*{box-sizing:border-box;margin:0;padding:0}
html,body{width:1200px;height:2256px;overflow:hidden}
body{background:var(--page);font-family:"Open Sans",Arial,sans-serif;color:var(--text);font-size:13px;position:relative}
.wrap{width:960px;margin:0 auto;position:relative}
h1,h2,h3,h4,.nav a,.tab{font-family:"Oswald",Arial,sans-serif}

/* hero */
.hero{position:relative;height:400px;background:linear-gradient(160deg,#3b2b22 0%,#8a5a3a 35%,#c58d5c 55%,#6e4a33 80%,#2d211b 100%)}
.site-header{position:absolute;top:0;left:0;right:0;height:92px;background:rgba(0,0,0,.72);z-index:2}
.utility{position:absolute;right:120px;top:8px;display:flex;align-items:center;gap:14px;color:#ccc;font-size:11px}
.utility .sq{width:14px;height:14px;background:#555;display:inline-block}
.utility .cta{background:var(--red);color:#fff;font-weight:700;padding:4px 12px;font-size:11px}
.brand{position:absolute;left:120px;top:14px;display:flex;align-items:center;gap:10px}
.brand .dot{width:56px;height:56px;border-radius:50%;background:var(--red)}
.brand span{font-family:"Oswald",Arial,sans-serif;font-weight:700;color:var(--red);font-size:20px;line-height:1.05;width:120px}
.nav{position:absolute;right:120px;top:50px;display:flex}
.nav a{color:#fff;text-decoration:none;font-size:13px;padding:10px 14px;letter-spacing:.5px}
.nav a.active{background:var(--red)}
.hero-arrow{position:absolute;top:290px;width:28px;height:40px;background:rgba(0,0,0,.6);display:flex;align-items:center;justify-content:center}
.hero-arrow.left{left:0}.hero-arrow.right{right:0}
.hero-caption{position:absolute;left:0;right:0;top:308px;height:62px;background:rgba(0,0,0,.55);display:flex;align-items:center;justify-content:center}
.hero-caption h1{color:var(--red);font-size:20px;font-weight:600;text-align:center;line-height:1.25;width:920px}
.hero-caption h1 b{color:#fff;font-weight:600}

/* ticker */
.ticker{height:40px;background:var(--red);color:#fff}
.ticker .wrap{display:flex;align-items:center;height:40px;gap:10px;font-size:11px}
.ticker .label{font-family:"Oswald",Arial,sans-serif;font-size:13px;width:80px}
.ticker .slot{background:#fff;color:var(--ink);height:24px;line-height:24px;padding:0 10px;width:240px;white-space:nowrap;overflow:hidden}
.ticker .expand{margin-left:auto;font-family:"Oswald",Arial,sans-serif;font-size:13px}

/* tabs */
.tabs{display:flex;justify-content:center;gap:44px;margin-top:36px;height:38px;border-bottom:1px solid var(--line)}
.tab{font-size:15px;color:#444;padding-top:6px}
.tab.active{color:var(--red);border-bottom:3px solid var(--red)}

/* filter + ad */
.filter-row{display:flex;gap:30px;margin-top:22px;height:170px}
.filter{width:230px}
.filter h4{color:var(--red);font-size:15px;font-weight:500;margin-bottom:10px}
.filter ul{list-style:none;display:grid;grid-template-columns:1fr 1fr;gap:9px 8px;font-size:11.5px}
.filter li{display:flex;align-items:center;gap:6px}
.filter li i{width:11px;height:11px;border:1px solid #999;border-radius:50%;display:inline-block}
.filter li.on i{background:var(--red);border-color:var(--red)}
.ad-banner{flex:1;height:140px;background:linear-gradient(90deg,#dfeef8,#9fcbe6 55%,#e8f3fa)}

/* cards */
.grid{display:grid;grid-template-columns:repeat(4,228px);gap:16px;margin-top:32px}
.card{background:var(--white);height:356px;border-bottom:3px solid var(--red);position:relative}
.card .photo{height:150px;position:relative}
.card .tag{position:absolute;left:0;bottom:0;background:var(--red);color:#fff;font-family:"Oswald",Arial,sans-serif;font-size:13px;padding:3px 12px}
.card h3{font-size:15px;color:var(--ink);font-weight:600;line-height:1.25;padding:12px 12px 8px}
.card p{font-size:11.5px;line-height:1.55;padding:0 12px}
.card .more{position:absolute;right:12px;bottom:12px;color:var(--red);font-size:11.5px;font-weight:600}
.ph-court{background:linear-gradient(135deg,#b9855a,#e0b283 50%,#7a5236)}
.ph-ice{background:linear-gradient(135deg,#c9d8e6,#f1f5f9 50%,#8aa3bb)}
.ph-grass{background:linear-gradient(135deg,#3d7a35,#7db556 55%,#2c5a28)}
.ph-clay{background:linear-gradient(135deg,#0f1f38,#27456f 55%,#0a1527)}
.ph-sand{background:linear-gradient(135deg,#d6b06d,#f0d59c 50%,#6ea2cf)}

.ad-wide{height:150px;margin-top:24px;background:linear-gradient(90deg,#f4f7fb,#bcd6ec 50%,#f4f7fb)}

/* info columns */
.info{display:grid;grid-template-columns:300px 300px 320px;gap:20px;margin-top:24px;height:290px}
.info .col{background:var(--white);padding:16px;border-top:3px solid var(--red)}
.info h2{color:var(--red);font-size:16px;font-weight:500;line-height:1.3;margin-bottom:8px}
.info p{font-size:11.5px;line-height:1.55;margin-bottom:8px}
.info ul{list-style:none;font-size:11.5px;line-height:1.5}
.info li{display:flex;gap:8px;margin-bottom:5px}
.info li:before{content:"";flex:0 0 7px;height:7px;margin-top:6px;background:var(--red)}
.news-head{display:flex;justify-content:space-between;align-items:baseline}
.news-head small{font-size:11px;color:var(--muted)}
.news-item{display:flex;gap:12px;margin-top:12px}
.date{width:46px;height:50px;background:var(--red);color:#fff;text-align:center;font-family:"Oswald",Arial,sans-serif;flex:0 0 46px}
.date b{display:block;font-size:20px;line-height:28px;font-weight:600}
.date span{font-size:11px;background:var(--night);display:block;line-height:22px}
.news-item p{margin:0}
.news-item strong{display:block;color:var(--ink);font-size:12px}

/* footer */
.site-footer{position:absolute;left:0;right:0;top:1968px;height:240px;background:var(--night)}
.site-footer .wrap{display:grid;grid-template-columns:180px 240px 300px 200px;gap:13px;padding-top:22px}
.site-footer h4{color:#fff;font-size:14px;font-weight:500;margin-bottom:10px;border-bottom:2px solid var(--red);display:inline-block;padding-bottom:3px}
.links{list-style:none;color:#bbb;font-size:11.5px;line-height:1.55}
.links li:before{content:"› ";color:var(--red)}
.tweet{display:flex;gap:10px;color:#bbb;font-size:11px;line-height:1.5;margin-bottom:14px}
.tweet i{width:36px;height:36px;background:#555;flex:0 0 36px}
.tweet b{color:var(--red);font-weight:600}
.video-main{height:110px;background:linear-gradient(135deg,#3a3a3a,#6b6b6b);position:relative}
.video-main svg{position:absolute;left:50%;top:50%;transform:translate(-50%,-50%)}
.thumbs{display:flex;gap:6px;margin-top:6px}
.thumbs i{flex:1;height:36px;background:#444}
.foot-brand{display:flex;flex-direction:column;align-items:center;gap:10px;padding-top:10px}
.foot-brand .dot{width:80px;height:80px;border-radius:50%;background:var(--red)}
.foot-brand span{font-family:"Oswald",Arial,sans-serif;font-weight:700;color:var(--red);font-size:18px;text-align:center}

.bottom-bar{position:absolute;left:0;right:0;top:2208px;height:48px;background:var(--red);color:#fff;font-size:11px}
.bottom-bar .wrap{display:flex;align-items:center;justify-content:space-between;height:48px}
.social{display:flex;gap:6px}
.social i{width:20px;height:20px;background:var(--red-dark);display:block}
</style>
</head>
<body>

<section class="hero" role="img" aria-label="Women's basketball players competing on court">
  <header class="site-header">
    <div class="utility">
      <span>(555) 010-4477</span><span>info@veloratv.net</span>
      <i class="sq"></i><i class="sq"></i><i class="sq"></i><i class="sq"></i>
      <span class="cta">GET BRISKLANE GAMES</span>
    </div>
    <div class="brand"><i class="dot"></i><span>VELORA ARENA CHANNEL</span></div>
    <nav class="nav">
      <a class="active">HOME</a><a>ABOUT US</a><a>WATCH</a><a>PROGRAMS</a><a>SPORTS</a><a>SCHEDULE</a><a>TOP STORIES</a><a>BLOGS</a><a>VIDEOS</a>
    </nav>
  </header>
  <span class="hero-arrow left"><svg width="10" height="14"><path d="M8 1 2 7l6 6" stroke="#fff" stroke-width="2" fill="none"/></svg></span>
  <span class="hero-arrow right"><svg width="10" height="14"><path d="M2 1l6 6-6 6" stroke="#fff" stroke-width="2" fill="none"/></svg></span>
  <div class="hero-caption">
    <h1>Lorem Ipsum Dolor Sit Amet Consectetuer <b>Lorem Ipsum Dolor Sit Amet Consectetuer</b> Lorem Ipsum Dolor Sit Amet Consectetuer Ipsum Dolor Sit Amet Consectetuer</h1>
  </div>
</section>

<div class="ticker">
  <div class="wrap">
    <span class="label">ON TODAY</span>
    <span class="slot">10:30 AM Lorem ipsum is the dummy text</span>
    <span class="slot">02:00 PM Lorem ipsum is the dummy text</span>
    <span class="slot">07:45 PM Lorem ipsum is the dummy text</span>
    <span class="expand">+ EXPAND SCHEDULE</span>
  </div>
</div>

<main class="wrap">
  <div class="tabs">
    <span class="tab active">ALL</span><span class="tab">BASKETBALL</span><span class="tab">HOCKEY</span><span class="tab">SOCCER</span><span class="tab">TENNIS</span><span class="tab">VOLLEYBALL</span>
  </div>

  <div class="filter-row">
    <div class="filter">
      <h4>Filter</h4>
      <ul>
        <li class="on"><i></i>All</li><li><i></i>Live Now</li>
        <li><i></i>Featured Videos</li><li><i></i>Pics of The Week</li>
        <li><i></i>Best Of 2015</li>
      </ul>
    </div>
    <div class="ad-banner" role="img" aria-label="Advertising banner for a partner agency"></div>
  </div>

  <div class="grid">
    <article class="card"><div class="photo ph-court" role="img" aria-label="Basketball game action"><span class="tag">Basketball</span></div><h3>LOREM IPSUM DOLOR SIT AMET CONSECTETUER</h3><p>Ut wisi enim ad minim veniam, quis nostrud exerci tation ullamcorper suscipit lobortis nisl ut aliquip ex ea commodo consequat duis autem.</p><span class="more">Read More</span></article>
    <article class="card"><div class="photo ph-ice" role="img" aria-label="Ice hockey players on the rink"><span class="tag">Hockey</span></div><h3>LOREM IPSUM DOLOR SIT AMET CONSECTETUER</h3><p>Ut wisi enim ad minim veniam, quis nostrud exerci tation ullamcorper suscipit lobortis nisl ut aliquip ex ea commodo consequat duis autem.</p><span class="more">Read More</span></article>
    <article class="card"><div class="photo ph-grass" role="img" aria-label="Soccer match on a grass pitch"><span class="tag">Soccer</span></div><h3>LOREM IPSUM DOLOR SIT AMET CONSECTETUER</h3><p>Ut wisi enim ad minim veniam, quis nostrud exerci tation ullamcorper suscipit lobortis nisl ut aliquip ex ea commodo consequat duis autem.</p><span class="more">Read More</span></article>
    <article class="card"><div class="photo ph-clay" role="img" aria-label="Tennis player serving"><span class="tag">Tennis</span></div><h3>LOREM IPSUM DOLOR SIT AMET CONSECTETUER</h3><p>Ut wisi enim ad minim veniam, quis nostrud exerci tation ullamcorper suscipit lobortis nisl ut aliquip ex ea commodo consequat duis autem.</p><span class="more">Read More</span></article>
    <article class="card"><div class="photo ph-sand" role="img" aria-label="Beach volleyball rally"><span class="tag">Volleyball</span></div><h3>LOREM IPSUM DOLOR SIT AMET CONSECTETUER</h3><p>Ut wisi enim ad minim veniam, quis nostrud exerci tation ullamcorper suscipit lobortis nisl ut aliquip ex ea commodo consequat duis autem.</p><span class="more">Read More</span></article>
    <article class="card"><div class="photo ph-grass" role="img" aria-label="Soccer players contesting the ball"><span class="tag">Soccer</span></div><h3>LOREM IPSUM DOLOR SIT AMET CONSECTETUER</h3><p>Ut wisi enim ad minim veniam, quis nostrud exerci tation ullamcorper suscipit lobortis nisl ut aliquip ex ea commodo consequat duis autem.</p><span class="more">Read More</span></article>
    <article class="card"><div class="photo ph-court" role="img" aria-label="Basketball player driving to the basket"><span class="tag">Basketball</span></div><h3>LOREM IPSUM DOLOR SIT AMET CONSECTETUER</h3><p>Ut wisi enim ad minim veniam, quis nostrud exerci tation ullamcorper suscipit lobortis nisl ut aliquip ex ea commodo consequat duis autem.</p><span class="more">Read More</span></article>
    <article class="card"><div class="photo ph-ice" role="img" aria-label="Hockey face-off on ice"><span class="tag">Hockey</span></div><h3>LOREM IPSUM DOLOR SIT AMET CONSECTETUER</h3><p>Ut wisi enim ad minim veniam, quis nostrud exerci tation ullamcorper suscipit lobortis nisl ut aliquip ex ea commodo consequat duis autem.</p><span class="more">Read More</span></article>
  </div>

  <div class="ad-wide" role="img" aria-label="Wide advertising banner for an online marketing partner"></div>

  <section class="info">
    <div class="col">
      <h2>What we offer to our visitors, we are more than just stats and replays</h2>
      <p>Ut wisi enim ad minim veniam, quis nostrud exerci tation ullamcorper suscipit lobortis nisl ut aliquip ex ea commodo consequat.</p>
      <ul>
        <li>Podcasts that discuss women's issues</li>
        <li>Blogs for women</li>
        <li>Digital Downloads for Fitness Programs</li>
        <li>Fitness Resources</li>
      </ul>
    </div>
    <div class="col">
      <h2>Solutions We Provide To the Women</h2>
      <p>Ut wisi enim ad minim veniam, quis nostrud exerci tation ullamcorper suscipit lobortis nisl ut aliquip ex ea commodo.</p>
      <ul>
        <li>Provides programming to an underserved market</li>
        <li>Provides expansive exposure (a critical ingredient) for the success of professional women's sports</li>
        <li>Values the athletic achievement of female athletes</li>
      </ul>
    </div>
    <div class="col">
      <div class="news-head"><h2>Latest News</h2><small>See All ›</small></div>
      <div class="news-item"><div class="date"><b>26</b><span>OCT</span></div><p><strong>Lorem ipsum dolor</strong>Ut wisi enim ad minim veniam quis nostrud exerci tation.</p></div>
      <div class="news-item"><div class="date"><b>27</b><span>OCT</span></div><p><strong>Lorem ipsum dolor</strong>Ut wisi enim ad minim veniam quis nostrud exerci tation.</p></div>
      <div class="news-item"><div class="date"><b>28</b><span>OCT</span></div><p><strong>Lorem ipsum dolor</strong>Ut wisi enim ad minim veniam quis nostrud exerci tation.</p></div>
    </div>
  </section>
</main>

<footer class="site-footer">
  <div class="wrap">
    <div>
      <h4>Quick Links</h4>
      <ul class="links"><li>Home</li><li>About Us</li><li>Watch</li><li>Program</li><li>Sports</li><li>Schedule</li><li>Top stories</li><li>Blogs</li><li>Videos</li></ul>
    </div>
    <div>
      <h4>Latest Tweets</h4>
      <div class="tweet"><i></i><p><b>@velora</b> Lorem ipsum is the dummy text of the industry, lorem ipsum dolor sit amet.</p></div>
      <div class="tweet"><i></i><p><b>@velora</b> Lorem ipsum is the dummy text of the industry, lorem ipsum dolor sit amet.</p></div>
    </div>
    <div>
      <h4>Latest Videos</h4>
      <div class="video-main" role="img" aria-label="Featured women's sports video still">
        <svg width="34" height="34" viewBox="0 0 34 34"><circle cx="17" cy="17" r="16" fill="rgba(0,0,0,.5)" stroke="#fff" stroke-width="2"/><path d="M13 10l11 7-11 7z" fill="#fff"/></svg>
      </div>
      <div class="thumbs"><i></i><i></i><i></i><i></i></div>
    </div>
    <div class="foot-brand"><i class="dot"></i><span>VELORA ARENA CHANNEL</span></div>
  </div>
</footer>

<div class="bottom-bar">
  <div class="wrap">
    <span>Copyright © 2015 Veloratv.net. All Rights Reserved.</span>
    <div class="social"><i></i><i></i><i></i><i></i><i></i></div>
  </div>
</div>

</body>
</html>
```